Playful Website Design Needed Pet Sitting and Dog Walking Business

Need a simple one page Web Design Built on WordPress.
Sections:

About Us
Services Provided
Costs
Contact Us
Intake Form (Questionnaire that goes to email)
See us in Action

Industry/Entity Type

Pet Sitting and Dog Walking

Number of Pages Required

1 page

Font styles to use
Other font styles liked:
• See the Business Card Font and use that.

Colors
EE7325
F08F49
F5BC92
FAE3D3
FDF4ED

Requirements
Must have
• See attached Logo Design, with Font's and Colors Use these as theme guide

```html
<!DOCTYPE html>
<html lang="en">
<head>
<meta charset="utf-8">
<title>Happy Tails Pet Care</title>
<link href="https://fonts.googleapis.com/css2?family=Patrick+Hand&family=Poppins:wght@400;500&display=swap" rel="stylesheet">
<style>
:root{
  --orange:#f26b1d;
  --orange-soft:#f08f49;
  --teal:#4b9db4;
  --teal-deep:#1f7a8c;
  --sky:#a5e0ef;
  --sky-pale:#cdf0f8;
  --mist:#f6f6f6;
  --ink:#2b2b2b;
  --grey:#5c5c5c;
  --white:#ffffff;
  --hand:"Patrick Hand",cursive;
  --body:"Poppins",sans-serif;
}
*{margin:0;padding:0;box-sizing:border-box}
html,body{width:1200px;height:3692px;overflow:hidden;background:var(--white)}
body{position:relative;font-family:var(--body);color:var(--ink)}
.abs{position:absolute}
.bg{position:absolute;left:0;top:0}
.hand{font-family:var(--hand);font-weight:400}
.brand{display:flex;align-items:center;gap:12px;font-family:var(--hand);font-size:34px;color:var(--orange);line-height:1}
.brand .dot{width:38px;height:38px;border-radius:50%;background:var(--orange-soft);flex:none}
.nav{top:28px;left:622px;display:flex;gap:38px;font-family:var(--hand);font-size:21px;color:var(--white)}
.btn{display:flex;align-items:center;justify-content:center;gap:8px;background:var(--orange);color:var(--white);font-family:var(--hand);font-size:15px;border-radius:24px;box-shadow:0 8px 16px rgba(242,107,29,.35)}
.btn svg{width:16px;height:16px}
.photo{border-radius:18px}
.eyebrow{font-family:var(--hand);color:var(--orange);font-size:21px;text-transform:uppercase}
.h2{font-family:var(--hand);font-size:40px;line-height:40px;color:var(--ink)}
.para{font-size:13.5px;line-height:23px;color:var(--grey)}
.hero-title{left:209px;top:202px;font-family:var(--hand);font-size:42px;line-height:54px;color:var(--white)}
.pill{display:inline-block;background:var(--white);color:var(--orange);border-radius:14px;padding:0 14px;margin-right:12px;margin-left:-20px}
.service{position:absolute;width:250px;text-align:center}
.service .pic{width:180px;height:150px;margin:0 auto;border-radius:50% 50% 46% 54%/58% 52% 48% 42%;border-top:5px solid #7cbf2b;border-right:5px solid #7cbf2b}
.service h3{font-family:var(--hand);color:var(--orange);font-size:24px;line-height:24px;margin-top:28px}
.service p{font-size:12.5px;line-height:20px;color:var(--grey);margin-top:14px}
.frame{position:absolute;border:6px solid var(--white);border-radius:10px;box-shadow:0 6px 18px rgba(0,0,0,.15)}
.perk{display:flex;align-items:center;gap:14px;font-family:var(--hand);font-size:23px;height:38px}
.perk svg{width:26px;height:26px}
.field{position:absolute;font-size:11px;color:var(--grey);border-bottom:1px solid #cfd8dc;padding-bottom:8px}
.card{left:205px;top:3011px;width:803px;height:383px;background:var(--white);border-radius:40px;box-shadow:0 10px 30px rgba(0,0,0,.08)}
.foot-links{left:619px;top:3440px;font-family:var(--hand);font-size:21px;color:var(--white);line-height:38px}
.foot-col{left:822px;top:3440px;font-family:var(--hand);color:var(--white)}
.social{display:flex;gap:16px;margin-top:10px}
.social span{width:12px;height:12px;border-radius:50%;background:var(--white)}
</style>
</head>
<body>

<!-- HERO -->
<svg class="bg" width="1200" height="640" viewBox="0 0 1200 640">
  <path d="M0 0H1200V520C1060 560 900 560 760 545C620 530 520 560 420 600C300 640 140 620 0 580Z" fill="var(--sky)"/>
  <path d="M0 0H1200V120C1060 150 900 150 780 230C700 290 690 400 610 470C520 540 380 560 240 560C140 560 60 555 0 545Z" fill="var(--teal)"/>
  <path d="M700 420C720 300 800 210 920 200C1040 190 1140 210 1200 230V540C1060 560 900 550 760 545C720 520 690 470 700 420Z" fill="var(--sky)"/>
  <path d="M190 0H400C410 60 370 120 300 150C240 175 200 140 190 90Z" fill="var(--white)"/>
</svg>

<div class="abs brand" style="left:196px;top:70px"><span class="dot"></span>Happy Tails</div>
<nav class="abs nav"><span>About Us</span><span>Services</span><span>Costs</span></nav>
<div class="abs btn" style="left:908px;top:23px;width:143px;height:46px">Contact Us <svg viewBox="0 0 16 16" fill="#fff"><circle cx="4" cy="6" r="2"/><circle cx="8" cy="3.5" r="2"/><circle cx="12" cy="6" r="2"/><ellipse cx="8" cy="11" rx="3.5" ry="3"/></svg></div>

<h1 class="hero-title">We Feed, Walk And Play With<br><span class="pill">Your Pet,</span>Eacch Visit!</h1>
<p class="abs" style="left:211px;top:322px;font-family:var(--hand);font-size:16px;line-height:25px;color:var(--white)">Lorem ipsum dolor sit amet, consectetur<br>adipiscing elit. Quam ut aliquam purus.</p>
<div class="abs btn" style="left:211px;top:399px;width:162px;height:44px">Book A Service <svg viewBox="0 0 16 16" fill="#fff"><circle cx="4" cy="6" r="2"/><circle cx="8" cy="3.5" r="2"/><circle cx="12" cy="6" r="2"/><ellipse cx="8" cy="11" rx="3.5" ry="3"/></svg></div>

<div class="abs" role="img" aria-label="Bowl of dry pet food" style="left:0;top:416px;width:208px;height:144px;border-radius:0 60% 50% 0;background:linear-gradient(160deg,#b07a45,#d9d9d9 70%)"></div>
<div class="abs" role="img" aria-label="Woman running with a dog on a leash" style="left:459px;top:200px;width:741px;height:430px;border-radius:50% 40% 30% 50%/60% 40% 50% 40%;background:radial-gradient(ellipse at 40% 55%,#b07c48,#8f6a45 40%,rgba(165,224,239,0) 72%)"></div>

<!-- ABOUT -->
<div class="abs" style="left:215px;top:695px;width:258px;height:309px;background:var(--orange);border-radius:60% 40% 30% 70%/40% 50% 50% 60%"></div>
<div class="abs photo" role="img" aria-label="Small dog lying beside its leash" style="left:235px;top:741px;width:339px;height:349px;border-radius:50px;background:linear-gradient(180deg,#f3efe9,#d8c7ae 60%,#a6733e);box-shadow:0 16px 30px rgba(110,90,160,.18)"></div>
<div class="abs eyebrow" style="left:670px;top:742px">About</div>
<h2 class="abs h2" style="left:670px;top:777px">What Exactly Does<br>Dog Walking Include<br>And Entail?</h2>
<p class="abs para" style="left:670px;top:910px;width:330px">Lorem Ipsum Dolor Sit Amet, Consectetur Adipiscing Elit. Quam Diam Ut Aliquam Purus. Et, Praesent Aliquet Et Non Lobortis Eget. Egestas Viverra Eu Gravida Pretium. Magna Sem Tristique Auctor Duis Et, A. Natoque Urna Quis Facilisi Risus Scelerisque Fermentum.</p>

<!-- SERVICES -->
<svg class="bg" style="top:1140px" width="1200" height="750" viewBox="0 0 1200 750">
  <path d="M0 0C120 40 220 80 420 60C620 40 760 100 900 80C1020 60 1120 30 1200 10V700C1100 690 1000 640 880 650C760 660 640 750 420 720C240 700 120 660 0 740Z" fill="var(--sky-pale)"/>
  <path d="M0 50C140 60 240 110 420 100C600 90 760 140 900 120C1020 100 1120 70 1200 60V660C1100 640 1000 610 880 620C760 630 640 700 420 680C240 660 120 620 0 690Z" fill="var(--mist)"/>
</svg>
<div class="abs eyebrow" style="left:0;width:1200px;text-align:center;top:1306px;text-transform:none">Services</div>
<h2 class="abs h2" style="left:0;width:1200px;text-align:center;top:1340px">What We Serve</h2>
<svg class="abs" style="left:90px;top:1420px" width="1020" height="150" viewBox="0 0 1020 150"><path d="M5 140C40 80 80 70 110 70M290 75C340 90 380 80 400 60M590 60C630 55 680 50 680 20C680 0 700 40 700 60M900 60C960 60 990 30 1010 10" fill="none" stroke="#8ab8c4" stroke-width="1.5" stroke-dasharray="5 5"/><path d="M990 10L1015 0L1005 22Z" fill="none" stroke="#5fb3c9" stroke-width="2"/></svg>
<div class="service" style="left:162px;top:1405px"><div class="pic" role="img" aria-label="Smiling pet sitter" style="background:linear-gradient(150deg,#c9a488,#8c5b44)"></div><h3>8$ Per Visit<br>2vicits A Day</h3><p>Lorem ipsum dolor sit amet, consectetur adipiscing elit. Quam diam ut aliquam purus. Et, praesent aliquet et non lobortis eget.</p></div>
<div class="service" style="left:475px;top:1405px"><div class="pic" role="img" aria-label="Group of small dogs" style="background:linear-gradient(150deg,#b9c3a8,#efeae0 50%,#7d6a4e)"></div><h3>All Pets, Any Age!</h3><p>Lorem ipsum dolor sit amet, consectetur adipiscing elit. Quam diam ut aliquam purus. Et, praesent aliquet et non lobortis eget.</p></div>
<div class="service" style="left:787px;top:1405px"><div class="pic" role="img" aria-label="Walker leading several dogs in a park" style="background:linear-gradient(150deg,#9bb0c6,#6d7a5a 55%,#4a3a30)"></div><h3>Parent Supervised</h3><p>Lorem ipsum dolor sit amet, consectetur adipiscing elit. Quam diam ut aliquam purus. Et, praesent aliquet et non lobortis eget.</p></div>
<div class="abs btn" style="left:519px;top:1735px;width:162px;height:46px">Book A Service <svg viewBox="0 0 16 16" fill="#fff"><circle cx="4" cy="6" r="2"/><circle cx="8" cy="3.5" r="2"/><circle cx="12" cy="6" r="2"/><ellipse cx="8" cy="11" rx="3.5" ry="3"/></svg></div>

<!-- WHY US -->
<div class="abs eyebrow" style="left:194px;top:1997px;text-transform:none">Action</div>
<h2 class="abs h2" style="left:194px;top:2034px">Why Us?</h2>
<p class="abs para" style="left:196px;top:2100px;width:285px">Lorem Ipsum Dolor Sit Amet, Consectetur Adipiscing Elit. Quam Diam Ut Aliquam Purus. Et, Praesent Aliquet Et Non Lobortis Eget. Egestas Viverra Eu Gravida Pretium. Magna Sem Tristique Auctor Duis Et, A. Natoque Urna Quis Facilisi Risus Scelerisque Fermentum.</p>
<div class="abs" style="left:200px;top:2293px">
  <div class="perk"><svg viewBox="0 0 26 26" fill="none" stroke="var(--orange)" stroke-width="2"><path d="M4 22V12l6-6 6 6v10M10 22v-6h4"/></svg>Trained</div>
  <div class="perk"><svg viewBox="0 0 26 26" fill="none" stroke="var(--orange)" stroke-width="2"><path d="M3 12h5v10H3zM8 13l5-8c2 0 3 1 2 4h7l-2 11H8"/></svg>Trusted</div>
  <div class="perk"><svg viewBox="0 0 26 26" fill="none" stroke="var(--orange)" stroke-width="2"><circle cx="13" cy="11" r="7"/><path d="M9 17l-2 7 6-3 6 3-2-7"/></svg>Certified</div>
</div>
<div class="frame" role="img" aria-label="Man walking a pack of dogs down a street" style="left:601px;top:2055px;width:165px;height:141px;background:linear-gradient(160deg,#a86a54,#6c8ab3 55%,#9a8f7e)"></div>
<div class="frame" role="img" aria-label="Woman walking several dogs in a city" style="left:783px;top:1951px;width:251px;height:364px;background:linear-gradient(170deg,#c5a58a,#e7d56a 35%,#8a6b50 70%,#c8b9a8)"></div>
<div class="frame" role="img" aria-label="Smiling woman petting dogs in a park" style="left:473px;top:2220px;width:270px;height:258px;background:linear-gradient(150deg,#b4ae9e,#7b3a4f 45%,#e9e4dc 75%,#9d8b72)"></div>
<div class="frame" role="img" aria-label="Close view of a brown dog" style="left:755px;top:2321px;width:233px;height:195px;background:linear-gradient(140deg,#6d5a46,#b0793f 50%,#3f332b)"></div>

<!-- CONTACT -->
<svg class="bg" style="top:2470px" width="1200" height="560" viewBox="0 0 1200 560">
  <path d="M0 70C200 110 400 90 600 70C820 50 1000 60 1200 80V560H0Z" fill="var(--mist)"/>
  <path d="M0 140C60 130 140 160 150 240C160 310 120 360 0 370Z" fill="#ececec"/>
</svg>
<div class="abs eyebrow" style="left:0;width:1200px;text-align:center;top:2663px">Contact Us</div>
<h2 class="abs h2" style="left:0;width:1200px;text-align:center;top:2697px">Looking For A Profesiional?</h2>
<p class="abs para" style="left:235px;top:2753px;width:730px;text-align:center">Lorem Ipsum Dolor Sit Amet, Consectetur Adipiscing Elit. Quam Diam Ut Aliquam Purus. Et, Praesent Aliquet Et Non Lobortis Eget. Egestas Viverra Eu Gravida Pretium. Magna Sem Tristique Auctor Duis Et, A. Natoque Urna Quis Facilisi Risus Scelerisque Fermentum.</p>
<div class="abs btn" style="left:513px;top:2842px;width:174px;height:44px;font-size:14px"><svg viewBox="0 0 16 16" fill="#fff"><path d="M3 1l3 3-2 2c1 2 3 4 5 5l2-2 3 3-2 3C7 15 1 9 1 3z"/></svg>(555) 014-3270</div>

<!-- FORM & FOOTER -->
<svg class="bg" style="top:2900px" width="1200" height="792" viewBox="0 0 1200 792">
  <path d="M300 60C330 20 420 25 520 30C700 40 900 40 1030 60C1070 90 1070 200 1040 360H280Z" fill="var(--sky-pale)"/>
  <path d="M1030 160C1090 140 1150 120 1200 110V792H0V560C220 560 420 520 520 470C620 420 700 350 800 300C880 260 980 180 1030 160Z" fill="var(--teal-deep)"/>
</svg>
<div class="abs card"></div>
<div class="abs" role="img" aria-label="Black bulldog puppy lying behind a leather leash" style="left:229px;top:3069px;width:345px;height:272px;border-radius:40%;background:radial-gradient(ellipse at 50% 45%,#2a2a2a 0,#3b3b3b 35%,#7a4a32 55%,rgba(255,255,255,0) 72%)"></div>
<div class="abs eyebrow" style="left:608px;top:3060px">Book A Service</div>
<h2 class="abs h2" style="left:608px;top:3087px">Intake Form</h2>
<svg class="abs" style="left:805px;top:3080px" width="64" height="24" viewBox="0 0 64 24"><path d="M2 8C20 4 44 4 62 6M10 18C28 14 44 14 56 15" stroke="#5fb3c9" stroke-width="2.5" fill="none" stroke-linecap="round"/></svg>
<div class="field" style="left:609px;top:3166px;width:158px">Name</div>
<div class="field" style="left:789px;top:3166px;width:158px">Phone</div>
<div class="field" style="left:609px;top:3200px;width:338px">Email</div>
<div class="field" style="left:609px;top:3234px;width:338px;height:48px">Type Here...</div>
<div class="abs btn" style="left:608px;top:3305px;width:162px;height:46px">Book A Service <svg viewBox="0 0 16 16" fill="#fff"><circle cx="4" cy="6" r="2"/><circle cx="8" cy="3.5" r="2"/><circle cx="12" cy="6" r="2"/><ellipse cx="8" cy="11" rx="3.5" ry="3"/></svg></div>

<div class="abs brand" style="left:150px;top:3470px"><span class="dot"></span>Happy Tails</div>
<div class="abs foot-links"><div>About Us</div><div>Services</div><div>Costs</div><div>Contact Us</div></div>
<div class="abs foot-col">
  <div style="font-size:21px;line-height:38px">Call Us</div>
  <div style="display:flex;align-items:center;gap:8px;font-size:14px;margin-top:2px"><span style="width:22px;height:22px;border-radius:50%;background:var(--orange-soft);display:flex;align-items:center;justify-content:center"><svg width="12" height="12" viewBox="0 0 16 16" fill="#fff"><path d="M3 1l3 3-2 2c1 2 3 4 5 5l2-2 3 3-2 3C7 15 1 9 1 3z"/></svg></span>(555) 014-3270</div>
  <div style="font-size:21px;line-height:38px;margin-top:10px">Follow Us</div>
  <div class="social"><span></span><span></span><span></span><span></span></div>
</div>
<svg class="abs" style="left:148px;top:3620px" width="910" height="14" viewBox="0 0 910 14"><path d="M0 12L908 2" stroke="#fff" stroke-width="1.5"/><path d="M860 3L908 0L904 12Z" fill="#fff"/></svg>
<p class="abs" style="left:148px;top:3654px;font-size:11.5px;color:var(--white)">©Copyright 2022. <span style="text-decoration:underline">HAPPY TAILS PET CARE</span> | All Rights Reserved</p>

</body>
</html>
```